Unique Hair Product needs upscale Tube Design

Velandra's Henna is a hair product company. I need a tube design for a 4oz ABL (soft aluminum) tube which incorporates my logo and product information and usage. The product is a high-end treatment for thicker, darker hair.

Velandra's Henna is a unique, strengthening color treatment, that will thicken weak, damaged hair, while enhancing hair color naturally, with henna.

Target Market(s)

Women age 17 and up

Industry/Entity Type

Hair Care Product

Requirements
Must have
• "Strengthening, Color enhancing, Hair treatment" this product description must be on the front of the tube. Please use diagram below.
• Must have logo placed strategically, and placed beautifully. I need the tube design to be elegant and beautiful because it is a high end product. Please use colors that you think would look nice and appeal to women. I was thinking a nice light olive green, with a white logo, but play with it until it looks really pretty.
• It will be going into a box, similar to the one below.
Nice to have
• Elegance, clarity and sharp
• please use the diagram to properly place the design in the designated space below
Should not have
• Please no cursive writing

```html
<!DOCTYPE html>
<html lang="en">
<head>
<meta charset="utf-8">
<title>Velandra's Henna – Tube Label</title>
<link rel="stylesheet" href="https://fonts.googleapis.com/css2?family=Cinzel:wght@400;500&family=Oswald:wght@300;400&family=Source+Sans+3:ital,wght@0,400;1,400&display=swap">
<style>
  :root {
    --olive: #7a8f55;
    --cream: #e6eadb;
    --page: #ffffff;
    --white: #f4f5ee;
  }
  * { margin: 0; padding: 0; box-sizing: border-box; }
  html, body {
    width: 1200px; height: 1000px; overflow: hidden;
    background: var(--page);
  }
  .canvas { position: relative; width: 1200px; height: 1000px; }
  .label {
    position: absolute; left: 282px; top: 139px;
    width: 636px; height: 722px;
    background: var(--olive);
  }
  .label-shapes { position: absolute; inset: 0; }
  .brand {
    position: absolute; left: 20px; top: 60px; width: 278px;
    display: flex; flex-direction: column; align-items: center;
    color: var(--white);
  }
  .brand-mark {
    width: 62px; height: 62px; border-radius: 50%;
    border: 2px solid var(--white);
  }
  .brand-name {
    margin-top: 42px;
    font-family: "Cinzel", serif; font-weight: 500; font-size: 22px; letter-spacing: 0.5px;
    white-space: nowrap;
  }
  .tagline-top {
    position: absolute; left: 338px; top: 80px; width: 276px;
    text-align: center;
    font-family: "Cinzel", serif; font-weight: 400; font-size: 19px; line-height: 38px;
    letter-spacing: 1.6px; color: var(--white); white-space: nowrap;
  }
  .description {
    position: absolute; left: 25px; top: 368px; width: 280px;
    text-align: center;
    font-family: "Source Sans 3", sans-serif; font-size: 14.5px; line-height: 20.5px;
    color: var(--olive);
  }
  .tagline-main {
    position: absolute; left: 0; top: 491px; width: 310px;
    text-align: center; white-space: nowrap;
    font-family: "Oswald", sans-serif; font-weight: 400; font-size: 36px; line-height: 51px;
    color: var(--olive);
  }
  .ingredients {
    position: absolute; left: 346px; top: 369px; width: 290px;
    font-family: "Source Sans 3", sans-serif; font-size: 14.5px; line-height: 20.3px;
    color: var(--olive);
  }
  .ingredients-title { font-style: italic; }
  .net-weight {
    position: absolute; left: 422px; top: 694px;
    font-family: "Source Sans 3", sans-serif; font-style: italic; font-size: 15px;
    color: var(--white);
  }
</style>
</head>
<body>
<div class="canvas">
  <section class="label">
    <svg class="label-shapes" width="636" height="722" viewBox="0 0 636 722" aria-hidden="true">
      <path d="M0,361 C138,361 198,226 318,226 C438,226 498,361 636,361 V684 H0 Z" fill="var(--cream)"/>
      <path d="M0,349 C138,349 198,214 318,214 C438,214 498,349 636,349" fill="none" stroke="var(--cream)" stroke-width="4"/>
      <rect x="0" y="672" width="636" height="6" fill="var(--olive)"/>
      <rect x="0" y="685" width="636" height="37" fill="var(--olive)"/>
    </svg>

    <div class="brand">
      <div class="brand-mark"></div>
      <div class="brand-name">VELANDRA'S HENNA</div>
    </div>

    <h2 class="tagline-top">STRENGTHENING<br>COLOR ENHANCING<br>HAIR TREATMENT</h2>

    <p class="description">Velandra's Henna is a unique,<br>strengthening color treatment,<br>that will thicken weak, damaged hair,<br>while enhancing hair color naturally,<br>with henna.</p>

    <h1 class="tagline-main">STRENGTHENING<br>COLOR ENHANCING<br>HAIR TREATMENT</h1>

    <div class="ingredients">
      <p class="ingredients-title">Ingredients:</p>
      <p>Lorem ipsum dolor sit amet,<br>consectetuer adipiscing elit.<br>In rutrum. Integer in sapien.<br>Fusce dui leo, imperdiet in,<br>aliquam sit amet, feugiat eu, orci.<br>Nullam eget nisl. Aliquam erat volutpat.<br>Proin pede metus, vulputate nec,<br>fermentum fringilla, vehicula vitae,<br>justo. Vivamus ac leo pretium faucibus.<br>Nullam rhoncus aliquam metus.<br>Proin mattis lacinia justo.</p>
    </div>

    <p class="net-weight">Netto:120g</p>
  </section>
</div>
</body>
</html>
```